Great Opportunity !! Masters in Business Analytics College Course

the size is Full Page, with bleed*
8”x 10.75" plus 0.25" bleed.
please leave one inch for footer
the purpose is attract students to join this college program .
this is for students in USA .
college age of around 24 years old
I am looking for a flyer that is unique and shows creativity .
A flyer that people would want to look at it because it is unique.
you can choose either vector, text ,or picture.
if you do picture it should be a white USA citizen wearing a white solid shirt and not long hair

Target Market(s)

USA students about 23 in age to join this college program

Industry/Entity Type

education

Colors
0054AA
0677BA
7BADD7
CADEEF
E8F1F8
0094D4
00A9DD
6FCCEA
C7EBF8
E9F6FB

Requirements
Must have
• the text should not be crowded .. .. .. the ad should not be full of text
Should not have
• not have very large text .. it should not be a flyer that is full of text .. you have to figure out how to avoid looking at the ad and it is very busy with text

```html
<!DOCTYPE html>
<html lang="en">
<head>
<meta charset="UTF-8">
<title>Master's in Business Analytics Flyer</title>
<link href="https://fonts.googleapis.com/css2?family=Bebas+Neue&family=Montserrat:ital,wght@0,400;0,500;0,700;1,800&display=swap" rel="stylesheet">
<style>
  :root {
    --page-bg: #e6e6e6;
    --flyer-blue: #2e84c6;
    --band-blue: #1c67a0;
    --accent-yellow: #fff200;
    --text-white: #ffffff;
    --footer-white: #ffffff;
    --footer-text: #e4e4e4;
  }
  * { margin: 0; padding: 0; box-sizing: border-box; }
  html, body { width: 920px; height: 1200px; overflow: hidden; background: var(--page-bg); }
  .flyer {
    position: absolute; left: 35px; top: 0;
    width: 850px; height: 1200px;
    background: var(--flyer-blue);
    overflow: hidden;
    color: var(--text-white);
  }
  .display { font-family: 'Bebas Neue', sans-serif; position: absolute; left: 41px; line-height: 1; z-index: 2; white-space: nowrap; transform-origin: left top; }
  .body-text { font-family: 'Montserrat', sans-serif; position: absolute; z-index: 2; }

  .headline { top: 42px; font-size: 66px; line-height: 60px; transform: scaleX(0.97); }

  .program-band {
    position: absolute; left: 0; top: 190px; width: 699px; height: 97px;
    background: var(--band-blue); border-radius: 0 49px 49px 0;
  }
  .program-band p {
    font-family: 'Montserrat', sans-serif; font-weight: 500;
    font-size: 30px; line-height: 38px; letter-spacing: 0.3px;
    position: absolute; left: 41px; top: 12px; text-transform: uppercase;
  }

  .prepare { top: 335px; font-size: 41px; line-height: 39px; }
  .median { top: 422px; font-size: 92px; transform: scaleX(0.97); }
  .salary { top: 504px; font-size: 96px; color: var(--accent-yellow); transform: scaleX(0.88); }
  .source { top: 598px; font-size: 43px; transform: scaleX(0.86); }

  .list-col { top: 668px; font-size: 18px; line-height: 21px; font-weight: 500; }
  .list-col h3 { font-size: 19.5px; font-weight: 500; line-height: 21px; margin-bottom: 8px; }
  .list-col ul { list-style: none; }
  .list-col li { display: flex; align-items: center; gap: 9px; line-height: 21.5px; padding-left: 3px; }
  .list-col li svg { width: 14px; height: 14px; flex: none; }
  .col-hired { left: 41px; }
  .col-roles { left: 222px; }
  .col-divider { position: absolute; left: 205px; top: 669px; width: 1.5px; height: 133px; background: var(--accent-yellow); }

  .open-house { position: absolute; left: 0; top: 832px; width: 422px; height: 104px; z-index: 2; }
  .open-house svg { position: absolute; inset: 0; }
  .open-house .oh-title { left: 41px; top: 14px; font-weight: 700; font-size: 22px; color: var(--accent-yellow); }
  .open-house .oh-date { left: 41px; top: 44px; font-weight: 700; font-size: 20px; }
  .open-house .oh-email { left: 41px; top: 73px; font-weight: 400; font-size: 15.5px; }

  .accreditation { left: 41px; top: 955px; font-size: 20px; line-height: 24px; }
  .accreditation strong { color: var(--accent-yellow); font-weight: 700; font-size: 21px; display: block; }

  .format { left: 41px; top: 1058px; font-size: 19px; font-weight: 800; font-style: italic; color: var(--accent-yellow); }

  .student-photo { position: absolute; left: 0; top: 0; width: 850px; height: 1098px; z-index: 1; }

  .footer-area {
    position: absolute; left: 0; top: 1098px; width: 850px; height: 102px;
    background: var(--footer-white); z-index: 3;
  }
  .footer-area span {
    position: absolute; left: 184px; top: 30px;
    font-family: 'Montserrat', sans-serif; font-weight: 500;
    font-size: 28px; letter-spacing: 27px; color: var(--footer-text);
  }
</style>
</head>
<body>
<main class="flyer">
  <h1 class="display headline">Do you have an analytical mind and<br>seeking a profitable career?</h1>

  <div class="program-band">
    <p>A Master's in Business Analytics<br>Ridgeline State University</p>
  </div>

  <p class="display prepare">Can prepare you for some of<br>the most in-demand jobs.</p>
  <p class="display median">With a median</p>
  <p class="display salary">Salary of $100K+</p>
  <p class="display source">(National Labor Data Office 2023)</p>

  <section class="body-text list-col col-hired">
    <h3>Graduates<br>were hired at:</h3>
    <ul>
      <li><svg viewBox="0 0 16 16"><rect x="1.5" y="2.5" width="12" height="12" rx="2" fill="none" stroke="#fff200" stroke-width="1.6"/><path d="M4.5 8.2l2.6 2.6L15 3" fill="none" stroke="#fff200" stroke-width="1.8"/></svg>Corvane</li>
      <li><svg viewBox="0 0 16 16"><rect x="1.5" y="2.5" width="12" height="12" rx="2" fill="none" stroke="#fff200" stroke-width="1.6"/><path d="M4.5 8.2l2.6 2.6L15 3" fill="none" stroke="#fff200" stroke-width="1.8"/></svg>Halden &amp; Pike</li>
      <li><svg viewBox="0 0 16 16"><rect x="1.5" y="2.5" width="12" height="12" rx="2" fill="none" stroke="#fff200" stroke-width="1.6"/><path d="M4.5 8.2l2.6 2.6L15 3" fill="none" stroke="#fff200" stroke-width="1.8"/></svg>Nexora</li>
      <li><svg viewBox="0 0 16 16"><rect x="1.5" y="2.5" width="12" height="12" rx="2" fill="none" stroke="#fff200" stroke-width="1.6"/><path d="M4.5 8.2l2.6 2.6L15 3" fill="none" stroke="#fff200" stroke-width="1.8"/></svg>Voltrane</li>
    </ul>
  </section>
  <div class="col-divider"></div>
  <section class="body-text list-col col-roles">
    <h3>Heading<br>Goes Here</h3>
    <ul>
      <li><svg viewBox="0 0 16 16"><rect x="1.5" y="2.5" width="12" height="12" rx="2" fill="none" stroke="#fff200" stroke-width="1.6"/><path d="M4.5 8.2l2.6 2.6L15 3" fill="none" stroke="#fff200" stroke-width="1.8"/></svg>BI Developer</li>
      <li><svg viewBox="0 0 16 16"><rect x="1.5" y="2.5" width="12" height="12" rx="2" fill="none" stroke="#fff200" stroke-width="1.6"/><path d="M4.5 8.2l2.6 2.6L15 3" fill="none" stroke="#fff200" stroke-width="1.8"/></svg>Data Analyst</li>
      <li><svg viewBox="0 0 16 16"><rect x="1.5" y="2.5" width="12" height="12" rx="2" fill="none" stroke="#fff200" stroke-width="1.6"/><path d="M4.5 8.2l2.6 2.6L15 3" fill="none" stroke="#fff200" stroke-width="1.8"/></svg>Data Scientist</li>
    </ul>
  </section>

  <section class="open-house">
    <svg viewBox="0 0 422 104" width="422" height="104"><polygon points="0,0 376,0 422,104 0,104" fill="#1c67a0"/></svg>
    <p class="body-text oh-title">OPEN HOUSE</p>
    <p class="body-text oh-date">Wednesday, April 20, 7:30 pm.</p>
    <p class="body-text oh-email">Email for the link! alex.morgan@mailbox.com</p>
  </section>

  <p class="body-text accreditation"><strong>GBSA Accreditation.</strong>A distinction held by only<br>5% of business schools globally.</p>

  <p class="body-text format">Hybrid / One Weekly Session</p>

  <svg class="student-photo" viewBox="0 0 850 1098" role="img" aria-label="Photo of a smiling young male student in a white polo shirt with a backpack, holding books and making an OK hand sign">
    <defs>
      <linearGradient id="studentTone" x1="0" y1="0" x2="0" y2="1">
        <stop offset="0" stop-color="#c9a58c"/>
        <stop offset="0.22" stop-color="#e6ddd8"/>
        <stop offset="0.45" stop-color="#f4f4f6"/>
        <stop offset="1" stop-color="#e6e8ee"/>
      </linearGradient>
    </defs>
    <path d="M640 464 C690 462 712 500 708 560 C705 600 692 615 690 625 L760 640 L790 620 L805 645 L850 690 L850 1098 L524 1098 L518 1000 L469 940 L478 860 L500 780 L520 700 L560 650 L600 630 C585 610 568 590 566 540 C564 495 595 466 640 464 Z" fill="url(#studentTone)"/>
  </svg>

  <footer class="footer-area"><span>1 INCH FOOTER</span></footer>
</main>
</body>
</html>
```